Velmar Cyber Security (Consultants)

We need a webdesign for a new website www.velmarcybersecurity.example.

A draft version of the website is online. You can also look at our linkedIn company page: http://www.linkedin.example/company/7412096

This is what we do:
We defend our cybersociety against the growing number of cyber threats in order to allow our society to prosper and evolve more safely into the digital age. We seek to protect 4 key pillars of our society: critical (industrial) infrastructures, medical systems, our intellectual property, and financial systems.

Velmar is specialised in IT & information security consultancy and positions itself as an independent partner. Our employees possess a unique mix of technical hands-on engineering and consulting skills. We invest time and resources to learn about existing open-source and commercial technologies in order to give better advice.

We are no-nonsense, practical and to the point.

We advise and guide organisations with the strategy, definition and technical implementation of security projects. We take ownership in aligning the existing business, operational and technical context.

Some requirements:
- Ideally you deliver a fully coded and designed static website. I am hosting the website on www.hostbay.example; you can use the technologies that are supported there.
- My existing company colors and logos need to be preserved (see existing websites & linkedIn page)
- I would like a white background (is the best fit for my existing logo's, and easiest to maintain afterwards)
Some examples, but please feel free: http://www.stoneward.example/ http://www.quevix.example/ )
- I will use twitter as a way to update my website with relevant news ; So I want the twitterfeed integrated in the website, certianly on the homepage; if possible on all pages. (www.twitter.example/velmarsecurity)
- I am using my linkedIn company page; I want at least the "Follow" company button to be integrated in the website. (http://www.linkedin.example/company/velmar-cybersecurity-consultants/)
- it should be possible for me to do some minor updates to the site.
- I need several nice banners that I could also re-use at my linkedIn webpage (linkedIn requires 646 x 220 pixels or larger banners)

- As I see it now, the website should have a Home page that immediately displays the core services we offer. A basic Jobs page. an about and contact page where people can leave their details behind.
- Optional: An industries tab where there are sub-sites possible
Updates

This project has just been garantueed! First and second place get a nice payment. Please send you designs. 

I need
- A ready to deploy basic HTML webpage
- 4 pages: Home, Services, Careers, About/contact
- Some nice banners designed on my mission statement (in the brief)

Thanks

Reason: We would like to receive some more designs from other designers.

Target Market(s)

From medium sized KMO's, to mainly big enterprises.
My focusses is on strategic consulting, So managers, decision takers & business people
The site should also attrack consultants that have technical skills and managerial skills...

Industry/Entity Type

Financial

Requirements
Must have
• - My existing company colors and logos need to be preserved (see existing websites & linkedIn page)
- I would like a clean, professional site, with a white background
- As I see it now, the website should have a Home page that immediately displays the core services we offer. A basic careers page. an about and contact page where people can leave their details behind.
Nice to have
• - it should be possible for me to do some minor updates to the site.

```html
<!DOCTYPE html>
<html lang="en">
<head>
<meta charset="utf-8">
<title>Velmar Cyber Security</title>
<link href="https://fonts.googleapis.com/css2?family=Source+Sans+3:wght@300;400;600&family=PT+Sans+Narrow:wght@400;700&display=swap" rel="stylesheet">
<style>
:root{
  --red:#c40f3a;
  --red-dark:#ad0a2c;
  --ink:#222;
  --text:#555;
  --muted:#777;
  --line:#d8d8d8;
  --band:#f2f2f2;
  --nav-top:#3e3e3e;
  --nav-bot:#1f1f1f;
  --foot:#3b3a3b;
  --foot-base:#2c2728;
  --foot-text:#b9b9b9;
}
*{margin:0;padding:0;box-sizing:border-box}
html,body{width:959px;height:1200px;overflow:hidden;background:#fff}
body{font-family:"Source Sans 3",sans-serif;color:var(--text);position:relative}
a{color:inherit;text-decoration:none}
ul{list-style:none}

.site-header{position:absolute;left:0;top:0;width:959px;height:106px}
.brand{position:absolute;left:68px;top:36px;display:flex;align-items:center;gap:10px}
.brand-dot{width:36px;height:36px;border-radius:50%;background:var(--red)}
.brand-name{font-size:42px;font-weight:400;color:var(--ink);letter-spacing:-.5px;line-height:1}
.util-nav{position:absolute;right:64px;top:12px;font-size:11px;color:var(--muted);font-weight:300}
.util-nav a{padding:0 6px}
.util-nav span{color:#aaa}
.search{position:absolute;left:686px;top:65px;width:210px;height:25px;border:1px solid #ddd;border-radius:3px;font-size:10px;font-style:italic;color:#999;padding:6px 10px}
.search svg{position:absolute;right:6px;top:5px}

.main-nav{position:absolute;left:0;top:106px;width:959px;height:39px;background:linear-gradient(var(--nav-top),var(--nav-bot));display:flex;padding-left:69px}
.main-nav a{font-family:"PT Sans Narrow",sans-serif;font-size:15px;color:#fff;line-height:39px;padding:0 18px;border-right:1px solid #555}
.main-nav a:first-child{padding-left:19px}
.main-nav a:last-child{border-right:none}

.hero{position:absolute;left:0;top:145px;width:959px;height:322px;overflow:hidden}
.hero-photo{position:absolute;left:360px;top:0;width:599px;height:322px;background:linear-gradient(90deg,rgba(255,255,255,1) 0%,rgba(196,204,214,.7) 25%,#8b97a6 55%,#5d6776 100%)}
.hero-copy{position:absolute;left:71px;top:72px;width:360px}
.hero-copy h1{font-size:28px;font-weight:600;color:var(--ink);letter-spacing:-.3px}
.hero-copy h2{font-size:20px;font-weight:400;color:#444;margin-top:2px}
.hero-copy p{font-size:11.5px;line-height:18px;color:#555;margin-top:8px}
.dots{display:flex;gap:3px;margin-top:16px}
.dots i{width:11px;height:11px;border-radius:50%;background:#ccc}
.dots i:first-child{background:var(--red)}

.features{position:absolute;left:0;top:467px;width:959px;height:151px;background:var(--band);border-top:1px solid #e6e6e6;border-bottom:1px solid #e6e6e6}
.feature{position:absolute;top:22px;width:260px}
.feature h3{font-size:22px;font-weight:400;color:var(--red);margin-left:3px}
.feature .icon{position:absolute;left:4px;top:44px;width:53px;height:53px;border-radius:50%}
.feature p{margin:8px 0 0 70px;font-size:10px;line-height:16px;color:var(--muted);font-weight:300}
.feature .more{display:block;margin:6px 0 0 71px;font-family:"PT Sans Narrow",sans-serif;font-weight:700;font-size:11.5px;color:#444}
.feature .more::after{content:"";display:inline-block;margin-left:4px;border-left:5px solid #444;border-top:4px solid transparent;border-bottom:4px solid transparent}
.divider{position:absolute;top:24px;width:1px;height:105px;background:var(--line)}

.video{position:absolute;left:70px;top:646px;width:280px}
.video h3,.news h3{font-size:22px;font-weight:400;color:#333}
.video-frame{position:relative;margin-top:10px;width:277px;height:150px;background:linear-gradient(90deg,#3a0d14 0%,#12344a 40%,#1d6b86 55%,#5a1018 85%,#2a0c10 100%)}
.play{position:absolute;left:118px;top:54px;width:40px;height:40px;border-radius:50%;background:rgba(255,255,255,.85)}
.play::after{content:"";position:absolute;left:15px;top:11px;border-left:14px solid #333;border-top:9px solid transparent;border-bottom:9px solid transparent}
.video h4{font-size:17px;font-weight:300;color:#444;margin-top:10px}
.video p{font-size:13px;font-weight:300;color:#666;margin-top:2px}

.news{position:absolute;left:380px;top:646px;width:218px}
.news h3{color:var(--red);font-size:20px;padding-bottom:2px;border-bottom:2px solid var(--red);position:relative}
.news h3::after{content:"";position:absolute;left:24px;bottom:-7px;border-top:6px solid var(--red);border-left:5px solid transparent;border-right:5px solid transparent}
.news li{margin-top:22px;padding-left:2px}
.news li+li{margin-top:14px}
.news h5{font-size:11px;font-weight:400;color:#333}
.news p{font-size:9.5px;line-height:14px;color:var(--muted);font-weight:300}
.news time{display:block;font-size:9.5px;color:var(--red);margin-top:3px;font-weight:300}

.why{position:absolute;left:636px;top:644px;width:264px;height:236px;border-radius:3px;background:linear-gradient(#d40a4a,#b2001f);padding:20px 24px 0 29px;color:#fff}
.why h3{font-size:20px;font-weight:600}
.why p{font-size:11px;line-height:18px;color:#fbd6de;margin-top:2px}
.why ul{margin-top:10px}
.why li{font-size:11px;font-weight:600;height:24px;line-height:24px;border-bottom:1px solid rgba(255,255,255,.25);display:flex;align-items:center;gap:5px;margin-left:-3px}
.why li:last-child{border-bottom:none}

.site-footer{position:absolute;left:0;top:920px;width:959px;height:223px;background:var(--foot)}
.foot-col{position:absolute;top:42px}
.foot-col h4{font-size:17px;font-weight:400;color:#eee;margin-bottom:5px}
.foot-col li{font-size:11px;line-height:18px;color:var(--foot-text);font-weight:300}
.social li{display:flex;align-items:center;gap:9px;line-height:20px}
.social i{width:15px;height:15px;border-radius:2px;background:#5b6f9a}
.social li:nth-child(2) i{background:#55a7d6}
.social li:nth-child(3) i{background:#2f79a9}
.social li:nth-child(4) i{background:#ee8a22}
.base{position:absolute;left:0;top:1143px;width:959px;height:57px;background:var(--foot-base);font-size:10px;color:#ccc;padding:25px 0 0 67px;font-weight:300}
</style>
</head>
<body>
<header class="site-header">
  <a class="brand" href="#"><span class="brand-dot"></span><span class="brand-name">Velmar</span></a>
  <nav class="util-nav"><a href="#">Client Login</a><span>|</span><a href="#">Get a Demo</a><span>|</span><a href="#">Customer Support</a><span>|</span><a href="#">Sitemap</a></nav>
  <div class="search">Search here
    <svg width="14" height="14" viewBox="0 0 14 14"><circle cx="6" cy="6" r="4.5" fill="none" stroke="#888" stroke-width="2"/><line x1="9.3" y1="9.3" x2="13" y2="13" stroke="#888" stroke-width="2.4"/></svg>
  </div>
</header>

<nav class="main-nav">
  <a href="#">HOME</a><a href="#">ABOUT US</a><a href="#">SERVICES</a><a href="#">PRODUCTS &amp; SOLUTIONS</a><a href="#">PARTNERS</a><a href="#">NEWS</a><a href="#">CAREER</a><a href="#">CONTACT</a>
</nav>

<section class="hero">
  <div class="hero-photo" role="img" aria-label="Security analyst working at a desk with several monitors"></div>
  <div class="hero-copy">
    <h1>Defenders of Our Cybersociety</h1>
    <h2>Donec scelerisque leo ac risus</h2>
    <p>Vivamus porttitor, g, purus nisi eleifend libero, a tempus libero lectus feugiat felis. Morbi diam mauris, viverra in, gravida eu, mattis in, ante. Morbi eget arcu. Morbi porta, libero id ullamcorper nonummy</p>
    <div class="dots"><i></i><i></i><i></i><i></i></div>
  </div>
</section>

<section class="features">
  <article class="feature" style="left:71px">
    <h3>Cybersecurity Strategy</h3>
    <div class="icon" role="img" aria-label="Radar screen icon" style="background:radial-gradient(circle at 40% 40%,#3fa7b5,#0f3d4a 70%,#c9c9c9 72%)"></div>
    <p>Morbi ornare gravida elit. Integer congue, augue et malesuada iaculis, ipsum dui aliquet felis at</p>
    <a class="more" href="#">LEARN MORE</a>
  </article>
  <div class="divider" style="left:331px"></div>
  <article class="feature" style="left:360px">
    <h3>Top-4 Cyber Controls</h3>
    <div class="icon" role="img" aria-label="Green number badge icon" style="background:radial-gradient(circle,#5bbf3a 55%,#e6e6e6 58%)"></div>
    <p>Morbi ornare gravida elit. Integer congue, augue et malesuada iaculis, ipsum dui aliquet felis at</p>
    <a class="more" href="#">LEARN MORE</a>
  </article>
  <div class="divider" style="left:619px"></div>
  <article class="feature" style="left:649px">
    <h3>Cyber Security</h3>
    <div class="icon" role="img" aria-label="Padlock icon" style="border-radius:6px;background:linear-gradient(#d0d0d0,#8a8a8a 60%,#e0b800 62%,#222 100%)"></div>
    <p>Morbi ornare gravida elit. Integer congue, augue et malesuada iaculis, ipsum dui aliquet felis at</p>
    <a class="more" href="#">LEARN MORE</a>
  </article>
</section>

<section class="video">
  <h3>Watch Our Video</h3>
  <div class="video-frame" role="img" aria-label="Video still of glowing padlocks over digital code"><span class="play"></span></div>
  <h4>Phasellus felis dolor, scelerisque</h4>
  <p>Tempus eget lobortis id libero Donec scelerisque.</p>
</section>

<section class="news">
  <h3>Latest News</h3>
  <ul>
    <li><h5>Curabitur iaculis tempus</h5><p>Donec scelerisque leo ac risus. Praesent sit amet est. In dictum, dolor eu dictum porttitor</p><time>Posted 2 day ago</time></li>
    <li><h5>Vivamus sollicitudin</h5><p>Donec scelerisque leo ac risus Praesent sit amet</p><time>Posted 2 day ago</time></li>
    <li><h5>Curabitur iaculis tempus</h5><p>Donec scelerisque leo ac risus. Praesent sit amet</p><time>Posted 2 day ago</time></li>
  </ul>
</section>

<aside class="why">
  <h3>Why Choose Us</h3>
  <p>Donec scelerisque leo ac risus. Praesent sit amet est. In dictum, dolor eu</p>
  <ul>
    <li><svg width="11" height="9" viewBox="0 0 11 9"><path d="M1 4.5l3 3L10 1" fill="none" stroke="#fff" stroke-width="2"/></svg>Morbi porta libero id ullamcorper</li>
    <li><svg width="11" height="9" viewBox="0 0 11 9"><path d="M1 4.5l3 3L10 1" fill="none" stroke="#fff" stroke-width="2"/></svg>Nonummy nibh ligula pulvinar</li>
    <li><svg width="11" height="9" viewBox="0 0 11 9"><path d="M1 4.5l3 3L10 1" fill="none" stroke="#fff" stroke-width="2"/></svg>Metus eget consectetuer</li>
    <li><svg width="11" height="9" viewBox="0 0 11 9"><path d="M1 4.5l3 3L10 1" fill="none" stroke="#fff" stroke-width="2"/></svg>Augue nisi quis lacus.</li>
    <li><svg width="11" height="9" viewBox="0 0 11 9"><path d="M1 4.5l3 3L10 1" fill="none" stroke="#fff" stroke-width="2"/></svg>Ut ac mi quis lacus mollis aliquam.</li>
  </ul>
</aside>

<footer class="site-footer">
  <div class="foot-col" style="left:68px"><h4>Company</h4><ul><li>About Us</li><li>Our Mission</li><li>Why Choose Us</li><li>Clients</li><li>Partners</li></ul></div>
  <div class="foot-col" style="left:202px"><h4>Our Services</h4><ul><li>Duis tincidunt</li><li>Lectus quis dui viverra</li><li>Suspendisse vulputate</li><li>Aliquam dui.</li><li>Nulla elementum dui ut augue.</li><li>Aliquam vehicula</li></ul></div>
  <div class="foot-col" style="left:402px"><h4>Products</h4><ul><li>Suspendisse vulputate</li><li>Aliquam dui.</li><li>Nulla elementum dui ut augue.</li><li>Aliquam vehicula</li></ul></div>
  <div class="foot-col" style="left:598px"><h4>Our Support</h4><ul><li>Customer Support</li><li>Latest News</li><li>Term of Use</li><li>Sitemap</li><li>Contact</li></ul></div>
  <div class="foot-col" style="left:758px"><h4>Get Connected</h4><ul class="social"><li><i></i>Friendwall</li><li><i></i>Chirpline</li><li><i></i>Linkwork</li><li><i></i>RSS</li></ul></div>
</footer>
<div class="base">Copyright © 2013 Company Name. All rights reserved.</div>
</body>
</html>
```